Business Card Design

We would like a colorful, engaging, welcoming business card, utilizing our picture of a local lighthouse. We are a Church. We would like the design to mostly feature the colour blue.
Updates
Project Deadline Extended
Reason: Because of some suggested changes that have been sent out
Thank you so much to all Designers who sent in submissions to us - it was really hard to make a decision, they were all of such high quality. We would not hesitate to recommend Sketch Harbor to other churches/ businesses.
Kestrel Beacon Fellowship
Industry/Entity Type
Business
Contact Information for Business Card
Kestrel Beacon Fellowship Inc, 17 Marrick Rd, TOVERDALE WA 6391, Ph: (08) 9517 4063, E: beaconfellowship@quorvamail.example, Chirpbook logo - Kestrel Beacon Fellowship Inc, Sunday Service 10am, "For God sent not his Son into the world to condemn the world; but that the world through Him might be saved." John 3:17.
Look and feel
Each slider illustrates characteristics of the customer's brand and the style your logo design should communicate.

```html
<!DOCTYPE html>
<html lang="en">
<head>
<meta charset="utf-8">
<title>Kestrel Beacon Fellowship, Inc – Business Card</title>
<link href="https://fonts.googleapis.com/css2?family=Lato:wght@400&display=swap" rel="stylesheet">
<style>
  :root {
    --seafoam: #9dd5cf;
    --sky: #3ec3e6;
    --title-blue: #1a74c0;
    --ink: #2b2b2b;
    --photo-deep: #1d3f8a;
    --photo-soft: #4f79b8;
  }
  html, body {
    margin: 0;
    padding: 0;
    overflow: hidden;
    background: #ffffff;
  }
  .card {
    position: relative;
    width: 1200px;
    height: 741px;
    background: var(--seafoam);
    overflow: hidden;
    font-family: "Lato", sans-serif;
    color: var(--ink);
  }
  .card__name {
    position: absolute;
    left: 28px;
    right: 0;
    top: 86px;
    margin: 0;
    text-align: center;
    font-weight: 400;
    font-size: 53px;
    line-height: 1;
    letter-spacing: 0.2px;
    color: var(--title-blue);
    white-space: nowrap;
  }
  .card__photo {
    position: absolute;
    left: 0;
    top: 160px;
    width: 438px;
    height: 581px;
    background: linear-gradient(to bottom, var(--photo-deep) 0%, var(--photo-soft) 100%);
  }
  .card__details {
    position: absolute;
    left: 438px;
    top: 160px;
    width: 762px;
    height: 276px;
    background: var(--sky);
  }
  .address,
  .phone {
    position: absolute;
    left: 190px;
    margin: 0;
    font-size: 40px;
    line-height: 52px;
    white-space: nowrap;
  }
  .address { top: 50px; font-style: normal; }
  .phone { top: 194px; }
  .card__online {
    position: absolute;
    left: 526px;
    top: 500px;
    font-size: 34px;
    line-height: 48px;
    white-space: nowrap;
  }
  .card__online p { margin: 0; }
</style>
</head>
<body>
  <main class="card">
    <h1 class="card__name">KESTREL BEACON FELLOWSHIP, INC</h1>

    <div class="card__photo" role="img" aria-label="Photograph of a local lighthouse on a headland at night"></div>

    <section class="card__details">
      <address class="address">17 Marrick Rd.<br>Toverdale WA 6391</address>
      <p class="phone">08.9517.4063</p>
    </section>

    <section class="card__online">
      <p class="email">beaconfellowship@quorvamail.example</p>
      <p class="social">Catch us on CHIRPBOOK</p>
    </section>
  </main>
</body>
</html>
```